Healthy Snack Bar Wrapper Design

We are passionate about delivering healthy and tasty treats that are Raw, Organic, Preservative Free, Gluten Free, have No Added Sugar and No Additives!
In this project we are looking for a design for a new healthy food product to be launched soon in Australia. The packaging will be a bar wrapper made from foil that will be hot sealed, with a front and a back.
The snack is a raw, organic and healthy treat made predominantly with nuts, and will come in 3 initial flavours:
- Velvet Harbor (Sour Cherry and Choc)
- Plum Fizzaroo (Banana, Apricot and Blueberry)
- Sunmelodia (Pineapple, Passionfruit and Kiwi)
The product name is MunchWell, which does not currently have a logo. We are happy to have this as a simple written component of the initial design at the top of the packaging, perhaps within an circle, square or oval.
The typeface used for the names and the main ingredients should be fun.
The overall design should be very simple and make use of minimal colours. Our preferences are to have a plain colour for the background, such as light organic brown or white, with an eye catching colour that can be used to define the flavour, but should not be too vibrant.
We do not want to have an 3 dimensional images or objects. Nor do we want to have product images and any imagery should be only to give the impression of the flavours within rather than an image of the flavour. Finally, we do not want to have gradients included in the design.
The final design should communicate healthy, tasty and fun!
Examples of inspiration designs are attached in the files.
Main Information:
- The front should comprise of the following information:
-- MunchWell
-- Flavour name (such as Velvet Harbor)
-- Main Ingredients (Sour Cherry and Choc) (This is optional)
-- Portion size (60g)
-- Message (This is optional)
--- 0% Additives
--- 60% Nuts
--- 100% Natural
- The back needs to have space for the following information:
-- Nutritional Information
-- Barcode
-- Ingredients
-- Contact information
- Wrapper Dimensions
-- Width: 14cm
-- Height: 15cm
- Bar Dimensions
-- Width: 3cm
-- Height: 10cm
-- Depth: 2.5cm
Target Market(s)
People who want to have a healthy tasty treat
Colors
Designer to choose colors to be used in the design.
Requirements
Must have
- Main Information:
- - The front should comprise of the following information:
- -- MunchWell
- -- Flavour name (such as Velvet Harbor)
- -- Main Ingredients (Sour Cherry and Choc) (This is optional)
- -- Portion size (60g)
- -- Message (This is optional)
- --- 0% Additives
- --- 60% Nuts
- --- 100% Natural
- - The back needs to have space for the following information:
- -- Nutritional Information
- -- Barcode
- -- Ingredients
- -- Contact information
- - Wrapper Dimensions
- -- Width: 14cm
- -- Height: 15cm
- - Bar Dimensions
- -- Width: 3cm
- -- Height: 10cm
- -- Depth: 2.5cm
Should not have
- We do not want to have an 3 dimensional images or objects. Nor do we want to have product images and any imagery should be only to give the impression of the flavours within rather than an image of the flavour. Finally, we do not want to have gradients included in the design.

```html
<!DOCTYPE html>
<html lang="en">
<head>
<meta charset="utf-8">
<title>MunchWell Bar Wrappers</title>
<link rel="stylesheet" href="https://fonts.googleapis.com/css2?family=Comfortaa:wght@500;600;700&display=swap">
<style>
  :root {
    --backdrop: #d6d6d6;
    --wrapper: #ffffff;
    --wrapper-edge: #c4c4c4;
    --seal-line: #e6e6e6;
    --ink: #1f1f1f;
    --brand-navy: #2b2a6e;
  }
  * { box-sizing: border-box; margin: 0; padding: 0; }
  html, body { width: 1200px; height: 597px; overflow: hidden; }
  body {
    background: var(--backdrop);
    font-family: "Comfortaa", "Trebuchet MS", sans-serif;
    color: var(--ink);
    position: relative;
  }
  .wrapper {
    position: absolute;
    top: 28px;
    width: 220px;
    height: 540px;
  }
  .wrapper--velvet { left: 130px; }
  .wrapper--plum { left: 490px; }
  .wrapper--sun { left: 850px; }
  .wrapper__foil {
    position: absolute;
    inset: 0;
    width: 220px;
    height: 540px;
  }
  .brand {
    position: absolute;
    left: 0;
    right: 0;
    top: 78px;
    height: 44px;
    display: flex;
    align-items: center;
    justify-content: center;
    gap: 8px;
  }
  .brand__dot {
    width: 14px;
    height: 14px;
    border-radius: 50%;
    background: var(--brand-navy);
  }
  .brand__name {
    font-size: 24px;
    font-weight: 600;
    color: var(--brand-navy);
  }
  .flavour {
    position: absolute;
    left: 26px;
    right: 20px;
    top: 144px;
  }
  .flavour__name {
    font-size: 20px;
    font-weight: 700;
    line-height: 1.1;
  }
  .flavour__ingredients {
    margin-top: 4px;
    font-size: 10px;
    font-weight: 600;
    line-height: 1.3;
  }
  .tagline {
    position: absolute;
    left: 26px;
    right: 10px;
    top: 212px;
    font-size: 46px;
    font-weight: 600;
    line-height: 1.05;
    letter-spacing: -1px;
  }
  .claims {
    position: absolute;
    left: 0;
    right: 0;
    top: 440px;
    text-align: center;
    font-size: 8px;
    font-weight: 700;
    line-height: 1.8;
  }
</style>
</head>
<body>

  <svg width="0" height="0" style="position:absolute" aria-hidden="true">
    <defs>
      <path id="foil-shape" d="M0,10 l5,-10 5,10 5,-10 5,10 5,-10 5,10 5,-10 5,10 5,-10 5,10 5,-10 5,10 5,-10 5,10 5,-10 5,10 5,-10 5,10 5,-10 5,10 5,-10 5,10 5,-10 5,10 5,-10 5,10 5,-10 5,10 5,-10 5,10 5,-10 5,10 5,-10 5,10 5,-10 5,10 5,-10 5,10 5,-10 5,10 5,-10 5,10 5,-10 5,10 5,-10 5,10 5,-10 5,10 V530 l-5,10 -5,-10 -5,10 -5,-10 -5,10 -5,-10 -5,10 -5,-10 -5,10 -5,-10 -5,10 -5,-10 -5,10 -5,-10 -5,10 -5,-10 -5,10 -5,-10 -5,10 -5,-10 -5,10 -5,-10 -5,10 -5,-10 -5,10 -5,-10 -5,10 -5,-10 -5,10 -5,-10 -5,10 -5,-10 -5,10 -5,-10 -5,10 -5,-10 -5,10 -5,-10 -5,10 -5,-10 -5,10 -5,-10 -5,10 -5,-10 -5,10 -5,-10 -5,10 -5,-10 Z"/>
    </defs>
  </svg>

  <article class="wrapper wrapper--velvet">
    <svg class="wrapper__foil" viewBox="0 0 220 540" aria-hidden="true">
      <use href="#foil-shape" fill="var(--wrapper)" stroke="var(--wrapper-edge)" stroke-width="1"/>
      <line x1="0" y1="58" x2="220" y2="58" stroke="var(--seal-line)" stroke-width="2"/>
      <line x1="0" y1="482" x2="220" y2="482" stroke="var(--seal-line)" stroke-width="2"/>
    </svg>
    <div class="brand"><span class="brand__dot"></span><span class="brand__name">MunchWell</span></div>
    <div class="flavour">
      <h2 class="flavour__name">Velvet Harbor</h2>
      <p class="flavour__ingredients">Sour Cherry &amp; Choc</p>
    </div>
    <p class="tagline">Taste<br>of<br>Health</p>
    <p class="claims">0% Additives | 60% Nuts | 100% Natural<br>60g</p>
  </article>

  <article class="wrapper wrapper--plum">
    <svg class="wrapper__foil" viewBox="0 0 220 540" aria-hidden="true">
      <use href="#foil-shape" fill="var(--wrapper)" stroke="var(--wrapper-edge)" stroke-width="1"/>
      <line x1="0" y1="58" x2="220" y2="58" stroke="var(--seal-line)" stroke-width="2"/>
      <line x1="0" y1="482" x2="220" y2="482" stroke="var(--seal-line)" stroke-width="2"/>
    </svg>
    <div class="brand"><span class="brand__dot"></span><span class="brand__name">MunchWell</span></div>
    <div class="flavour">
      <h2 class="flavour__name">Plum Fizzaroo</h2>
      <p class="flavour__ingredients">Banana, Apricot &amp; Blueberry</p>
    </div>
    <p class="tagline">Taste<br>of<br>Health</p>
    <p class="claims">0% Additives | 60% Nuts | 100% Natural<br>60g</p>
  </article>

  <article class="wrapper wrapper--sun">
    <svg class="wrapper__foil" viewBox="0 0 220 540" aria-hidden="true">
      <use href="#foil-shape" fill="var(--wrapper)" stroke="var(--wrapper-edge)" stroke-width="1"/>
      <line x1="0" y1="58" x2="220" y2="58" stroke="var(--seal-line)" stroke-width="2"/>
      <line x1="0" y1="482" x2="220" y2="482" stroke="var(--seal-line)" stroke-width="2"/>
    </svg>
    <div class="brand"><span class="brand__dot"></span><span class="brand__name">MunchWell</span></div>
    <div class="flavour">
      <h2 class="flavour__name">Sunmelodia</h2>
      <p class="flavour__ingredients">Pineapple, Passionfruit<br>&amp; Kiwi</p>
    </div>
    <p class="tagline">Taste<br>of<br>Health</p>
    <p class="claims">0% Additives | 60% Nuts | 100% Natural<br>60g</p>
  </article>

</body>
</html>
```